RT Website Home Page Design

The task is to develop a winning design for a replacement website for our client RT Plumbing, Heating, AC & Remodeling. ct

```html
<!DOCTYPE html>
<html lang="en">
<head>
<meta charset="utf-8">
<title>RT Plumbing, Heating, AC &amp; Remodeling</title>
<link href="https://fonts.googleapis.com/css2?family=Poppins:wght@400;500;600;700&display=swap" rel="stylesheet">
<style>
:root{
  --navy:#1d2a5b;
  --navy-deep:#17214a;
  --yellow:#f5d937;
  --red:#d7262d;
  --text:#333a4d;
  --muted:#6b7080;
  --white:#ffffff;
}
*{box-sizing:border-box;margin:0;padding:0}
html,body{width:1200px;height:4862px;overflow:hidden}
body{font-family:"Poppins",sans-serif;color:var(--text);background:var(--white);position:relative}
a{color:inherit;text-decoration:none}

/* header */
.site-header{position:absolute;left:0;top:0;width:1200px;height:117px;background:var(--white)}
.brand{position:absolute;left:88px;top:30px;display:flex;align-items:center;gap:12px}
.brand-dot{width:22px;height:22px;border-radius:50%;background:var(--yellow);flex:none}
.brand-name{width:210px;font-weight:600;font-size:15px;color:var(--navy);line-height:1.3}
.header-info{position:absolute;left:425px;top:38px;font-size:13px;color:var(--muted);text-align:center;width:350px}
.header-info strong{display:block;color:var(--navy);font-size:15px;font-weight:600;margin-top:2px}
.btn-outline{position:absolute;left:940px;top:19px;width:172px;height:34px;border:1.5px solid #9aa0b2;border-radius:17px;font-size:13px;color:var(--navy);display:flex;align-items:center;justify-content:center}
.btn-quote{position:absolute;left:940px;top:64px;width:172px;height:34px;border-radius:17px;background:var(--yellow);font-size:13px;color:var(--navy);display:flex;align-items:center;justify-content:center}
.main-nav{position:absolute;left:0;top:117px;width:1200px;height:40px;background:var(--navy);display:flex;align-items:center;padding-left:103px}
.main-nav a{color:var(--white);font-size:13px;padding:4px 11px;border-radius:13px}
.main-nav a.active{background:var(--yellow);color:var(--navy)}

/* hero */
.hero{position:absolute;left:0;top:157px;width:1200px;height:580px;overflow:hidden}
.hero-photo{position:absolute;inset:0;background:linear-gradient(100deg,#dfe3ea 0%,#c7ccd6 38%,#9a7b5a 65%,#6c5742 100%)}
.hero svg{position:absolute;left:0;top:0}
.hero-title{position:absolute;left:700px;top:140px;width:390px;text-align:center;color:var(--yellow);font-size:39px;font-weight:600;line-height:1.22}
.btn-start{position:absolute;left:827px;top:318px;width:144px;height:34px;border-radius:17px;background:var(--navy);border:1.5px solid var(--white);color:var(--white);font-size:13px;display:flex;align-items:center;justify-content:center}

/* services */
.section-title{position:absolute;width:1200px;text-align:center;font-size:25px;font-weight:600;color:var(--navy)}
.service{position:absolute;width:200px;text-align:center}
.service-circle{width:132px;height:132px;margin:0 auto;border-radius:50%;background:var(--white);box-shadow:0 4px 14px rgba(0,0,0,.08);border:4px solid transparent;border-bottom-color:var(--yellow);border-left-color:var(--yellow);transform:rotate(-20deg);display:flex;align-items:center;justify-content:center}
.service-circle svg{transform:rotate(20deg)}
.service-label{margin-top:20px;font-size:15px;font-weight:500;color:var(--navy);line-height:1.45}
.service.featured{background:var(--white);box-shadow:0 4px 16px rgba(0,0,0,.1);padding:20px 0 26px;width:222px}
.service.featured .service-circle{background:var(--navy);border-color:var(--navy)}

/* request form */
.request{position:absolute;left:0;top:1349px;width:1200px;height:562px}
.request>svg{position:absolute;inset:0}
.request-title{position:absolute;top:86px;width:1200px;text-align:center;color:var(--white);font-size:25px;font-weight:500}
.field{position:absolute;height:36px;background:var(--white);border-radius:3px;display:flex;align-items:center;gap:10px;padding-left:18px;font-size:12px;color:#8a8f9c}
.field.area{height:94px;align-items:flex-start;padding-top:14px}
.btn-submit{position:absolute;left:542px;top:430px;width:115px;height:32px;border-radius:16px;background:#1f3f9a;color:var(--white);font-size:13px;display:flex;align-items:center;justify-content:center}

/* features */
.photo{position:absolute}
.feature-title{position:absolute;font-size:25px;font-weight:600;color:var(--navy)}
.feature-body{position:absolute;font-size:13.5px;line-height:1.78;color:var(--text)}

/* savings */
.savings{position:absolute;left:0;top:2736px;width:1200px;height:652px}
.savings>svg{position:absolute;inset:0}
.savings-title{position:absolute;top:76px;width:1200px;text-align:center;color:var(--white);font-size:25px;font-weight:600}
.offer{position:absolute;top:144px;width:320px;height:332px;background:var(--yellow);overflow:hidden}
.offer-photo{position:absolute;left:0;top:0;width:320px;height:160px}
.offer-curve{position:absolute;left:0;top:120px}
.offer-name{position:absolute;left:24px;top:192px;font-size:22px;font-weight:600;color:var(--navy);line-height:1.22}
.offer-note{position:absolute;left:24px;top:270px;font-size:14px;color:var(--navy);line-height:1.35}
.badge{position:absolute;left:208px;top:150px;width:92px;height:90px}
.badge svg{position:absolute;inset:0}
.badge span{position:absolute;left:0;width:92px;text-align:center;color:var(--white);font-weight:600;line-height:1}
.btn-details{position:absolute;left:511px;top:527px;width:178px;height:34px;border-radius:17px;border:1.5px solid var(--white);color:var(--white);font-size:13.5px;display:flex;align-items:center;justify-content:center}

/* blog */
.post{position:absolute;top:3536px;width:320px;height:386px;background:var(--white);box-shadow:0 3px 14px rgba(0,0,0,.1)}
.post-photo{width:320px;height:197px}
.post-date{position:absolute;left:26px;top:224px;font-size:12px;color:var(--muted);display:flex;gap:12px;align-items:center}
.post-title{position:absolute;left:26px;top:260px;width:270px;font-size:15.5px;font-weight:500;color:var(--navy);line-height:1.5}
.btn-read{position:absolute;left:24px;top:330px;width:116px;height:30px;border-radius:15px;background:var(--navy);color:var(--white);font-size:12px;display:flex;align-items:center;justify-content:center}
.btn-read.alt{background:var(--yellow);color:var(--navy)}
.btn-view{position:absolute;left:542px;top:3965px;width:116px;height:31px;border-radius:16px;background:var(--navy);color:var(--white);font-size:13px;display:flex;align-items:center;justify-content:center}

/* footer */
.site-footer{position:absolute;left:0;top:4076px;width:1200px;height:786px;color:var(--white)}
.site-footer>svg{position:absolute;inset:0}
.footer-brand{position:absolute;left:89px;top:168px;display:flex;align-items:center;gap:12px}
.footer-brand .brand-name{color:var(--white);width:220px;font-size:16px}
.contact{position:absolute;left:89px;display:flex;gap:18px;align-items:center;font-size:15px;line-height:1.5}
.contact-icon{width:38px;height:38px;border-radius:50%;background:var(--white);display:flex;align-items:center;justify-content:center}
.contact small{font-size:11px}
.footer-col{position:absolute;font-size:12.5px;line-height:25.5px}
.footer-col h4{color:var(--yellow);font-size:15px;font-weight:600;line-height:1.3;margin-bottom:4px}
.footer-col a.current{color:var(--yellow);text-decoration:underline}
.footer-bar{position:absolute;left:0;top:746px;width:1200px;height:40px;background:var(--navy-deep)}
.copyright{position:absolute;left:89px;top:12px;font-size:13px}
.pay{position:absolute;top:10px;width:34px;height:20px;border-radius:3px;background:#e9ecf3}
.social{position:absolute;left:1086px;top:9px;width:22px;height:22px;border-radius:50%;background:#3a5aa8}
.to-top{position:absolute;left:1148px;top:700px}
</style>
</head>
<body>

<header class="site-header">
  <div class="brand">
    <span class="brand-dot"></span>
    <span class="brand-name">RT Plumbing, Heating, AC &amp; Remodeling</span>
  </div>
  <div class="header-info">Serving Brookvale, MA &amp; Neighboring Communities.<strong>508.555.0142 &nbsp;|&nbsp; 800.555.0179</strong></div>
  <a class="btn-outline">Request Service</a>
  <a class="btn-quote">Request a Quote</a>
</header>

<nav class="main-nav">
  <a class="active">About</a><a>Plumbing</a><a>Water Heaters</a><a>Heating</a><a>Air Conditioning</a><a>Indoor Air Quality</a><a>Commercial</a><a>Handy Work &amp; Remodeling</a><a>Contact</a>
</nav>

<section class="hero">
  <div class="hero-photo" role="img" aria-label="Company service van parked in front of a home"></div>
  <svg width="1200" height="580" viewBox="0 0 1200 580">
    <path d="M0,420 C300,560 800,520 1200,360 L1200,580 L0,580 Z" fill="#f5d937"/>
    <path d="M0,480 C340,650 850,590 1200,400 L1200,580 L0,580 Z" fill="#ffffff"/>
  </svg>
  <h1 class="hero-title">Enjoy the Best of Home Living. Indoors &amp; Out.</h1>
  <a class="btn-start">Get Started</a>
</section>

<h2 class="section-title" style="top:802px">More of What You Need</h2>

<div class="service" style="left:158px;top:872px">
  <div class="service-circle"><svg width="56" height="56" viewBox="0 0 56 56" fill="none" stroke="#1d2a5b" stroke-width="2.5"><path d="M8 10h14v30a6 6 0 0 0 12 0V22h14"/><path d="M16 10v30a14 14 0 0 0 28 0V30"/><path d="M40 18h10v8H40z"/></svg></div>
  <div class="service-label">Plumbing</div>
</div>
<div class="service" style="left:387px;top:872px">
  <div class="service-circle"><svg width="56" height="56" viewBox="0 0 56 56" fill="none" stroke="#1d2a5b" stroke-width="2.5"><rect x="16" y="6" width="24" height="40" rx="3"/><circle cx="28" cy="22" r="6"/><path d="M22 36h12M22 50v-4M34 50v-4"/></svg></div>
  <div class="service-label">Water Heaters</div>
</div>
<div class="service" style="left:613px;top:872px">
  <div class="service-circle"><svg width="56" height="56" viewBox="0 0 56 56" fill="none" stroke="#1d2a5b" stroke-width="2.5"><path d="M6 28L28 8l22 20M12 24v24h32V24"/><path d="M20 44c-3-4 3-6 0-10M28 44c-3-4 3-6 0-10M36 44c-3-4 3-6 0-10"/></svg></div>
  <div class="service-label">Heating</div>
</div>
<div class="service" style="left:840px;top:872px">
  <div class="service-circle"><svg width="56" height="56" viewBox="0 0 56 56" fill="none" stroke="#1d2a5b" stroke-width="2.5"><rect x="6" y="12" width="44" height="18" rx="3"/><path d="M12 24h32M18 36c-2 3 2 5 0 8M26 36c-2 3 2 5 0 8M34 36c-2 3 2 5 0 8M42 36c-2 3 2 5 0 8"/></svg></div>
  <div class="service-label">Air Conditioning</div>
</div>

<div class="service" style="left:158px;top:1079px">
  <div class="service-circle"><svg width="56" height="56" viewBox="0 0 56 56" fill="none" stroke="#1d2a5b" stroke-width="2.5"><path d="M6 20h30a6 6 0 1 0-6-6M6 30h40a6 6 0 1 1-6 6M10 40h20"/></svg></div>
  <div class="service-label">Indoor Air Quality</div>
</div>
<div class="service" style="left:387px;top:1079px">
  <div class="service-circle"><svg width="56" height="56" viewBox="0 0 56 56" fill="none" stroke="#1d2a5b" stroke-width="2.5"><path d="M6 12h44M10 12v6h36v-6"/><rect x="12" y="22" width="8" height="24" rx="2"/><rect x="24" y="22" width="8" height="24" rx="2"/><rect x="36" y="22" width="8" height="24" rx="2"/></svg></div>
  <div class="service-label">Water Filtration</div>
</div>
<div class="service" style="left:613px;top:1079px">
  <div class="service-circle"><svg width="56" height="56" viewBox="0 0 56 56" fill="none" stroke="#1d2a5b" stroke-width="2.5"><path d="M6 28L28 8l22 20M12 24v24h32V24"/><path d="M22 44l14-14M32 30l6 6"/></svg></div>
  <div class="service-label">Remodeling &amp;<br>Handy Work</div>
</div>
<div class="service featured" style="left:829px;top:1059px">
  <div class="service-circle"><svg width="56" height="56" viewBox="0 0 56 56" fill="none" stroke="#f5d937" stroke-width="2.5"><rect x="8" y="12" width="40" height="30" rx="2"/><path d="M14 42v6M42 42v6M28 36c-6 0-7-6-3-10 0 3 2 4 3 2 1-4 6-4 5 2 0 4-2 6-5 6z"/></svg></div>
  <div class="service-label">Gas Fireplaces</div>
</div>

<section class="request">
  <svg width="1200" height="562" viewBox="0 0 1200 562">
    <path d="M0,47 Q600,-30 1200,47 L1200,40 Q600,-45 0,40 Z" fill="#f5d937"/>
    <path d="M0,47 Q600,-10 1200,47 L1200,511 Q600,590 0,511 Z" fill="#1f2b55" role="img" aria-label="Dimly lit living room background"/>
    <path d="M0,511 Q600,590 1200,511 L1200,520 Q600,615 0,520 Z" fill="#f5d937"/>
  </svg>
  <h2 class="request-title">Request Service</h2>
  <div class="field" style="left:342px;top:147px;width:249px"><svg width="12" height="12" viewBox="0 0 12 12" fill="#1f3f9a"><circle cx="6" cy="3.5" r="3"/><path d="M0 12c0-4 12-4 12 0z"/></svg>Name</div>
  <div class="field" style="left:608px;top:147px;width:249px"><svg width="12" height="12" viewBox="0 0 12 12" fill="#1f3f9a"><path d="M6 0a4 4 0 0 1 4 4c0 3-4 8-4 8S2 7 2 4a4 4 0 0 1 4-4z"/></svg>Address</div>
  <div class="field" style="left:342px;top:200px;width:249px"><svg width="14" height="12" viewBox="0 0 14 12" fill="#1f3f9a"><path d="M0 12V4h4V0h6v12z"/></svg>City</div>
  <div class="field" style="left:608px;top:200px;width:249px"><svg width="14" height="10" viewBox="0 0 14 10" fill="#1f3f9a"><rect width="14" height="10" rx="2"/></svg>Zip</div>
  <div class="field" style="left:342px;top:255px;width:249px"><svg width="14" height="10" viewBox="0 0 14 10" fill="#1f3f9a"><path d="M0 0h14v10H0z"/></svg>Email</div>
  <div class="field" style="left:608px;top:255px;width:249px"><svg width="9" height="13" viewBox="0 0 9 13" fill="#1f3f9a"><rect width="9" height="13" rx="1.5"/></svg>Phone</div>
  <div class="field area" style="left:342px;top:310px;width:515px"><svg width="12" height="13" viewBox="0 0 12 13" fill="#1f3f9a"><rect width="12" height="13" rx="1"/></svg>Comments</div>
  <a class="btn-submit">Submit</a>
</section>

<div class="photo" role="img" aria-label="Plumber repairing a kitchen sink faucet with a wrench" style="left:89px;top:1995px;width:490px;height:296px;background:linear-gradient(135deg,#c9b9a3,#8e8a86 55%,#5e5852)"></div>
<h2 class="feature-title" style="left:659px;top:2054px">Back to School Reminder</h2>
<p class="feature-body" style="left:659px;top:2104px;width:440px">Most families see an uptick in morning "rush hour" activity once the school year begins, and so does your water heater. Can yours keep up with the increased demand? Contact us today for a water heater check-up and free quote on a replacement system.</p>

<h2 class="feature-title" style="left:89px;top:2390px">The RT Difference Makers</h2>
<p class="feature-body" style="left:89px;top:2432px;width:460px">RT is a favorite choice among homeowners who appreciate our extensive range of home comfort and related services. Others like us best for our 100% satisfaction guarantee, while still others enjoy the many benefits that membership in our Preferred Service Club provides. Add it all up, and there's a lot to like about RT Plumbing, Heating, AC &amp; Remodeling.</p>
<div class="photo" role="img" aria-label="Technician with clipboard greeting a homeowner" style="left:621px;top:2336px;width:490px;height:296px;background:linear-gradient(135deg,#3a4256,#7b5a4e 50%,#a9a7a4)"></div>

<section class="savings">
  <svg width="1200" height="652" viewBox="0 0 1200 652">
    <path d="M0,40 Q600,-25 1200,40 L1200,32 Q600,-40 0,32 Z" fill="#f5d937"/>
    <path d="M0,40 Q600,-5 1200,40 L1200,600 Q600,660 0,600 Z" fill="#1d2a5b" role="img" aria-label="Dark blurred home interior background"/>
    <path d="M0,600 Q600,660 1200,600 L1200,610 Q600,680 0,610 Z" fill="#f5d937"/>
  </svg>
  <h2 class="savings-title">Enjoy the Savings...Plus the Added Comfort!</h2>

  <article class="offer" style="left:89px">
    <div class="offer-photo" role="img" aria-label="Technician servicing a water heater" style="background:linear-gradient(135deg,#e9ecef,#b8b4a8)"></div>
    <svg class="offer-curve" width="320" height="80" viewBox="0 0 320 80"><path d="M0,60 Q160,10 320,40 L320,80 L0,80 Z" fill="#1d2a5b"/><path d="M0,70 Q160,22 320,52 L320,80 L0,80 Z" fill="#f5d937"/></svg>
    <div class="offer-name">NEW WATER<br>HEATER</div>
    <div class="offer-note">on a new water heater,<br>tank-style or tankless.</div>
    <div class="badge"><svg width="92" height="90" viewBox="0 0 92 90"><path d="M6,0 H86 V54 L46,90 L6,54 Z" fill="#d7262d"/><rect x="6" y="38" width="80" height="2" fill="#fff"/></svg><span style="top:10px;font-size:22px">$120</span><span style="top:46px;font-size:17px">SAVE</span></div>
  </article>

  <article class="offer" style="left:440px">
    <div class="offer-photo" role="img" aria-label="Outdoor HVAC condenser units" style="background:linear-gradient(135deg,#d6dde4,#8f9aa6)"></div>
    <svg class="offer-curve" width="320" height="80" viewBox="0 0 320 80"><path d="M0,60 Q160,10 320,40 L320,80 L0,80 Z" fill="#1d2a5b"/><path d="M0,70 Q160,22 320,52 L320,80 L0,80 Z" fill="#f5d937"/></svg>
    <div class="offer-name">HVAC<br>SYSTEM</div>
    <div class="offer-note">on a new heating or<br>cooling system.</div>
    <div class="badge"><svg width="92" height="90" viewBox="0 0 92 90"><path d="M6,0 H86 V54 L46,90 L6,54 Z" fill="#d7262d"/><rect x="6" y="38" width="80" height="2" fill="#fff"/></svg><span style="top:10px;font-size:22px">$350</span><span style="top:46px;font-size:17px">SAVE</span></div>
  </article>

  <article class="offer" style="left:791px">
    <div class="offer-photo" role="img" aria-label="Business handshake in a bright office" style="background:linear-gradient(135deg,#eef1f4,#b5c0cf)"></div>
    <svg class="offer-curve" width="320" height="80" viewBox="0 0 320 80"><path d="M0,60 Q160,10 320,40 L320,80 L0,80 Z" fill="#1d2a5b"/><path d="M0,70 Q160,22 320,52 L320,80 L0,80 Z" fill="#f5d937"/></svg>
    <div class="offer-name">FIRST-TIME<br>CUSTOMER</div>
    <div class="offer-note" style="top:284px">on any service we provide.</div>
    <div class="badge"><svg width="92" height="90" viewBox="0 0 92 90"><path d="M6,0 H86 V54 L46,90 L6,54 Z" fill="#d7262d"/><rect x="6" y="38" width="80" height="2" fill="#fff"/></svg><span style="top:10px;font-size:22px">$35</span><span style="top:46px;font-size:17px">SAVE</span></div>
  </article>

  <a class="btn-details">Click for Details</a>
</section>

<h2 class="section-title" style="top:3466px">Latest Blog</h2>

<article class="post" style="left:89px">
  <div class="post-photo" role="img" aria-label="Green houseplant leaves in a white pot" style="background:linear-gradient(135deg,#f3f4f0,#7fa050)"></div>
  <div class="post-date"><svg width="14" height="14" viewBox="0 0 14 14" fill="none" stroke="#6b7080" stroke-width="1.4"><rect x="1" y="2" width="12" height="11" rx="1.5"/><path d="M1 6h12M4 0v3M10 0v3"/></svg>May 22, 2023</div>
  <h3 class="post-title">Best Houseplants for Cleaner Indoor Air</h3>
  <a class="btn-read">Read More</a>
</article>
<article class="post" style="left:440px">
  <div class="post-photo" role="img" aria-label="Road signs pointing in opposite directions under a blue sky" style="background:linear-gradient(180deg,#6d9bd2,#b6cde8)"></div>
  <div class="post-date"><svg width="14" height="14" viewBox="0 0 14 14" fill="none" stroke="#6b7080" stroke-width="1.4"><rect x="1" y="2" width="12" height="11" rx="1.5"/><path d="M1 6h12M4 0v3M10 0v3"/></svg>April 29, 2023</div>
  <h3 class="post-title">AC Myths You Should Stop Believing</h3>
  <a class="btn-read">Read More</a>
</article>
<article class="post" style="left:791px">
  <div class="post-photo" role="img" aria-label="Brass water heater valve close-up" style="background:linear-gradient(135deg,#d9cfb8,#8e7750)"></div>
  <div class="post-date"><svg width="14" height="14" viewBox="0 0 14 14" fill="none" stroke="#6b7080" stroke-width="1.4"><rect x="1" y="2" width="12" height="11" rx="1.5"/><path d="M1 6h12M4 0v3M10 0v3"/></svg>April 12, 2023</div>
  <h3 class="post-title">Is An Old Water Heater Dangerous?</h3>
  <a class="btn-read alt">Read More</a>
</article>
<a class="btn-view">View All</a>

<footer class="site-footer">
  <svg width="1200" height="786" viewBox="0 0 1200 786">
    <path d="M0,130 Q500,10 1200,0 L1200,60 Q600,50 0,150 Z" fill="#f5d937"/>
    <path d="M0,150 Q600,55 1200,60 L1200,786 L0,786 Z" fill="#1d2a5b"/>
  </svg>
  <div class="footer-brand"><span class="brand-dot"></span><span class="brand-name">RT Plumbing, Heating, AC &amp; Remodeling</span></div>
  <div class="contact" style="top:280px"><span class="contact-icon"><svg width="14" height="18" viewBox="0 0 14 18" fill="#1d2a5b"><path d="M7 0a7 7 0 0 1 7 7c0 5-7 11-7 11S0 12 0 7a7 7 0 0 1 7-7z"/><circle cx="7" cy="7" r="2.5" fill="#fff"/></svg></span><span>118 Linden Street<br>Brookvale, MA 01899</span></div>
  <div class="contact" style="top:352px"><span class="contact-icon"><svg width="16" height="16" viewBox="0 0 16 16" fill="#1d2a5b"><path d="M3 0l3 4-2 2c1 2 4 5 6 6l2-2 4 3-2 3C8 16 0 8 0 2z"/></svg></span><span>508.555.0142 <small>(Local)</small><br>800.555.0179 <small>(Toll Free)</small></span></div>

  <div class="footer-col" style="left:440px;top:134px"><h4>ABOUT</h4>Company Profile<br>Guarantees &amp; Assurances<br><a class="current">Priority Service Club</a><br>Employment<br>Areas Served</div>
  <div class="footer-col" style="left:660px;top:134px"><h4>PLUMBING</h4>Service &amp; Repair<br>Plumbing Installations<br>Outdoor Plumbing<br>Sewer &amp; Drain<br>Frozen Pipes<br>Gas Piping<br>Sump Pumps<br>Water Leak Detection &amp; Repair<br>Gas Piping</div>
  <div class="footer-col" style="left:910px;top:134px"><h4>HEATING</h4>Preventive Maintenance<br>Boiler Service &amp; Repair<br>Furnace Service &amp; Repair<br>Boiler<br>Furnace<br>Gas Fireplace Insert</div>

  <div class="footer-col" style="left:440px;top:416px"><h4>HANDY WORK &amp;<br>REMODELING</h4>Overview<br>Bathroom<br>Kitchens<br>Decks, Porches &amp; Patios<br>Basement<br>Windows &amp; Doors<br>Gas Fireplace<br>Interior &amp; Exterior<br>Handyman Services</div>
  <div class="footer-col" style="left:660px;top:416px"><h4>AIR CONDITIONING</h4>Preventive Maintenance<br>Service &amp; Repair<br>New AC System<br>Ductless Air System</div>
  <div class="footer-col" style="left:910px;top:416px"><h4>WATER HEATERS</h4>Service &amp; Repair<br>Tank-style Water Heater<br>Tankless Water Heater<br>Combi Boiler</div>
  <div class="footer-col" style="left:660px;top:576px"><h4>INDOOR AIR QUALITY</h4>Air Cleaners<br>Duct Sealing<br>Humidity Control</div>
  <div class="footer-col" style="left:910px;top:576px"><h4>COMMERCIAL</h4>Plumbing<br>HVAC</div>

  <svg class="to-top" width="20" height="22" viewBox="0 0 20 22"><path d="M10 0L20 22L10 16L0 22Z" fill="#ffffff"/></svg>

  <div class="footer-bar">
    <div class="copyright">© 2023 RT Plumbing. All Right Reserved</div>
    <span class="pay" style="left:912px"></span>
    <span class="pay" style="left:952px"></span>
    <span class="pay" style="left:992px"></span>
    <span class="pay" style="left:1032px"></span>
    <span class="social"></span>
  </div>
</footer>

</body>
</html>
```